hi all

Im after a new age looking business card with my company logo on it

must include these details, I would like the PH and Email to be symbols

If the colours used for card could be kept within the colours used in logo that I have supplied that would be great, if another colour is to be used dark grey would be ok. no light bulbs etc thanks

Details below to be incorporated on card

Damian Holloway

Lic E871302

PH 0219647381

E info@brightvaleelectrical.example.nz

Domestic Commercial Industrial Electricians

```html
<!DOCTYPE html>
<html lang="en">
<head>
<meta charset="utf-8">
<title>Brightvale Electrical – Business Card</title>
<link href="https://fonts.googleapis.com/css2?family=Jost:wght@200&family=Arimo:wght@400&display=swap" rel="stylesheet">
<style>
  :root {
    --backdrop: #9a9a9a;
    --card: #f4f4f3;
    --ink-dark: #2b2b2b;
    --ink-grey: #4a4a4a;
    --brand-blue: #1f6db3;
    --frame-line: #b9c3d3;
  }
  html, body {
    margin: 0;
    width: 1200px;
    height: 1200px;
    overflow: hidden;
    background: var(--backdrop);
  }
  .card {
    position: absolute;
    left: 100px;
    top: 300px;
    width: 1000px;
    height: 600px;
    background: var(--card);
    border-radius: 36px;
  }
  .card__name {
    position: absolute;
    left: 0;
    right: 0;
    top: 120px;
    text-align: center;
    font-family: "Jost", sans-serif;
    font-weight: 200;
    font-size: 64px;
    letter-spacing: 0.32em;
    color: var(--ink-dark);
    margin: 0;
  }
  .brand-block {
    position: absolute;
    left: 90px;
    top: 330px;
    width: 400px;
    height: 210px;
    border: 1px solid var(--frame-line);
    display: flex;
    flex-direction: column;
    align-items: center;
    justify-content: center;
    gap: 16px;
  }
  .brand-block__dot {
    width: 46px;
    height: 46px;
    border-radius: 50%;
    background: var(--brand-blue);
  }
  .brand-block__name {
    font-family: "Arimo", sans-serif;
    font-weight: 400;
    font-size: 36px;
    letter-spacing: 0.06em;
    color: var(--brand-blue);
    text-transform: uppercase;
    text-align: center;
    line-height: 1.1;
    margin: 0;
  }
  .contact {
    position: absolute;
    left: 530px;
    top: 335px;
    font-family: "Arimo", sans-serif;
    font-size: 25px;
    line-height: 1.28;
    color: var(--ink-grey);
    list-style: none;
    margin: 0;
    padding: 0;
  }
  .contact__row {
    display: flex;
    align-items: center;
    gap: 10px;
  }
  .contact__icon {
    width: 24px;
    height: 24px;
    flex: none;
  }
  .contact__spacer {
    width: 24px;
    flex: none;
  }
  .contact__services {
    padding-left: 34px;
    margin-top: 4px;
  }
</style>
</head>
<body>
  <main class="card">
    <h1 class="card__name">Damian Holloway</h1>

    <div class="brand-block">
      <span class="brand-block__dot"></span>
      <p class="brand-block__name">Brightvale Electrical</p>
    </div>

    <ul class="contact">
      <li class="contact__row"><span class="contact__spacer"></span>Lic E871302</li>
      <li class="contact__row">
        <svg class="contact__icon" viewBox="0 0 24 24" aria-label="Phone">
          <path fill="var(--ink-dark)" d="M6.6 10.8a15.1 15.1 0 0 0 6.6 6.6l2.2-2.2a1 1 0 0 1 1-.25 11.4 11.4 0 0 0 3.6.57 1 1 0 0 1 1 1V20a1 1 0 0 1-1 1A17 17 0 0 1 3 4a1 1 0 0 1 1-1h3.5a1 1 0 0 1 1 1c0 1.25.2 2.45.57 3.57a1 1 0 0 1-.25 1z"/>
        </svg>
        PH 0219647381
      </li>
      <li class="contact__row">
        <svg class="contact__icon" viewBox="0 0 24 24" aria-label="Email">
          <rect x="2" y="5" width="20" height="14" fill="none" stroke="var(--ink-dark)" stroke-width="1.6"/>
          <path d="M2 5l10 8 10-8M2 19l7.5-7M22 19l-7.5-7" fill="none" stroke="var(--ink-dark)" stroke-width="1.6"/>
        </svg>
        E info@brightvaleelectrical.example.nz
      </li>
      <li class="contact__services">Domestic Commercial<br>Industrial Electricians</li>
    </ul>
  </main>
</body>
</html>
```